BRAVEN EV

We need a business card design for a new Luxury golf cart Company Braven. We manufacture and sell high end golf carts. We would like to see designs that are high end. I have the logo so really need a nice clean look.

```html
<!DOCTYPE html>
<html lang="en">
<head>
<meta charset="utf-8">
<title>Lorva EV – Business Card</title>
<link rel="stylesheet" href="https://fonts.googleapis.com/css2?family=Crimson+Pro:wght@600;700&display=swap">
<style>
  :root {
    --backdrop: #555555;
    --card-grey: #858786;
    --teal-deep: #00433a;
    --teal-dark: #005f50;
    --teal-bright: #009a82;
    --teal-ink: #00614f;
    --icon-grey: #8a8c8b;
    --white: #ffffff;
  }
  html, body {
    margin: 0;
    padding: 0;
    width: 1200px;
    height: 1200px;
    overflow: hidden;
    background: var(--backdrop);
    font-family: "Crimson Pro", Georgia, serif;
  }
  .canvas {
    position: relative;
    width: 1200px;
    height: 1200px;
  }
  .card {
    position: absolute;
    width: 533px;
    height: 305px;
    background: var(--card-grey);
    overflow: hidden;
  }
  .card--front { left: 228px; top: 216px; }
  .card--back  { left: 402px; top: 601px; }
  .card__wave {
    position: absolute;
    inset: 0;
    width: 533px;
    height: 305px;
  }
  .brand-name {
    position: absolute;
    left: 0;
    width: 540px;
    top: 72px;
    margin: 0;
    text-align: center;
    font-weight: 700;
    font-size: 54px;
    letter-spacing: 0.14em;
    color: var(--teal-ink);
    line-height: 1;
  }
  .person {
    position: absolute;
    left: 115px;
    width: 303px;
    top: 16px;
    text-align: right;
  }
  .person__name {
    margin: 0;
    font-weight: 700;
    font-size: 38px;
    letter-spacing: 0.05em;
    color: var(--teal-ink);
    line-height: 1;
    text-align: left;
    white-space: nowrap;
  }
  .person__role {
    margin: 2px -0.25em 0 0;
    font-weight: 600;
    font-size: 19px;
    letter-spacing: 0.25em;
    color: var(--teal-ink);
    line-height: 1;
  }
  .contacts {
    list-style: none;
    margin: 0;
    padding: 0;
  }
  .contact {
    position: absolute;
    left: 140px;
    height: 44px;
    display: flex;
    align-items: center;
  }
  .contact__icon {
    width: 46px;
    height: 44px;
    display: flex;
    align-items: center;
    justify-content: center;
  }
  .contact__text {
    position: absolute;
    left: 81px;
    white-space: nowrap;
    font-weight: 700;
    font-size: 22px;
    letter-spacing: 0.22em;
    color: var(--white);
  }
  .contact--phone { top: 118px; }
  .contact--phone .contact__text { letter-spacing: 0.3em; }
  .contact--email { top: 175px; }
  .contact--web   { top: 234px; }
  .contact--web .contact__text { letter-spacing: 0.2em; }
</style>
</head>
<body>
<main class="canvas">

  <section class="card card--front" aria-label="Card front">
    <svg class="card__wave" viewBox="0 0 533 305" aria-hidden="true">
      <defs>
        <linearGradient id="frontWave" x1="0" y1="194" x2="0" y2="305" gradientUnits="userSpaceOnUse">
          <stop offset="0" stop-color="var(--teal-deep)"/>
          <stop offset="0.4" stop-color="var(--teal-bright)"/>
          <stop offset="0.65" stop-color="var(--teal-bright)"/>
          <stop offset="1" stop-color="var(--teal-dark)"/>
        </linearGradient>
      </defs>
      <path d="M0 230 C60 214 110 194 151 194 C230 194 320 239 430 239 C480 239 515 225 533 217 L533 305 L0 305 Z" fill="url(#frontWave)"/>
    </svg>
    <h1 class="brand-name">LORVA</h1>
  </section>

  <section class="card card--back" aria-label="Card back">
    <svg class="card__wave" viewBox="0 0 533 305" aria-hidden="true">
      <defs>
        <linearGradient id="backWave" x1="0" y1="0" x2="533" y2="0" gradientUnits="userSpaceOnUse">
          <stop offset="0" stop-color="var(--teal-dark)"/>
          <stop offset="0.9" stop-color="var(--teal-bright)"/>
          <stop offset="1" stop-color="#008f79"/>
        </linearGradient>
      </defs>
      <path d="M0 88 C40 72 80 66 120 66 C230 66 300 111 384 111 C440 111 490 88 533 74 L533 305 L0 305 Z" fill="url(#backWave)"/>
    </svg>

    <div class="person">
      <p class="person__name">NAME SURNAME</p>
      <p class="person__role">Job Position</p>
    </div>

    <ul class="contacts">
      <li class="contact contact--phone">
        <span class="contact__icon">
          <svg width="26" height="32" viewBox="0 0 26 32" aria-hidden="true">
            <path d="M8 2 C3 6 2 14 7 22 C11 28 16 31 20 30" fill="none" stroke="var(--icon-grey)" stroke-width="3" stroke-linecap="round"/>
            <path d="M8 2 L11 8 M20 30 L17 24" stroke="var(--icon-grey)" stroke-width="3" stroke-linecap="round"/>
          </svg>
        </span>
        <span class="contact__text">555-555-555</span>
      </li>
      <li class="contact contact--email">
        <span class="contact__icon">
          <svg width="36" height="24" viewBox="0 0 36 24" aria-hidden="true">
            <rect x="1" y="1" width="34" height="22" fill="none" stroke="var(--icon-grey)" stroke-width="2"/>
            <path d="M1 1 L18 14 L35 1" fill="none" stroke="var(--icon-grey)" stroke-width="2"/>
          </svg>
        </span>
        <span class="contact__text">info.lorva.com</span>
      </li>
      <li class="contact contact--web">
        <span class="contact__icon">
          <svg width="44" height="44" viewBox="0 0 44 44" aria-hidden="true">
            <g fill="none" stroke="var(--icon-grey)" stroke-width="1.6">
              <circle cx="22" cy="22" r="20"/>
              <ellipse cx="22" cy="22" rx="9" ry="20"/>
              <line x1="22" y1="2" x2="22" y2="42"/>
              <line x1="2" y1="22" x2="42" y2="22"/>
              <line x1="6" y1="12" x2="38" y2="12"/>
              <line x1="6" y1="32" x2="38" y2="32"/>
            </g>
          </svg>
        </span>
        <span class="contact__text">www.lorva.com</span>
      </li>
    </ul>
  </section>

</main>
</body>
</html>
```